Residential & commercial landscaping company

Updated business cards for commercial and landscaping company. We would like to keep out logo, but just need a more updated business card.

```html
<!DOCTYPE html>
<html lang="en">
<head>
<meta charset="UTF-8">
<title>GreenReach Business Cards</title>
<link href="https://fonts.googleapis.com/css2?family=Arimo:wght@400;700&display=swap" rel="stylesheet">
<style>
  :root {
    --bg: #c9c9c9;
    --leaf: #5a8139;
    --lime: #8cc63f;
    --grass: #6dbb45;
    --paper: #ffffff;
    --ink: #111111;
  }
  html, body {
    margin: 0;
    padding: 0;
    width: 1200px;
    height: 788px;
    overflow: hidden;
    background: var(--bg);
    font-family: "Arimo", Arial, sans-serif;
  }
  .sheet {
    position: relative;
    width: 1200px;
    height: 788px;
  }
  .card {
    position: absolute;
    width: 540px;
    height: 309px;
    border-radius: 22px;
    overflow: hidden;
    box-shadow: 0 6px 18px rgba(0,0,0,0.25);
  }
  .card--front { left: 40px; top: 240px; background: var(--paper); }
  .card--back { left: 620px; top: 240px; background: var(--leaf); }
  .card__wave { position: absolute; inset: 0; }
  .brand {
    position: absolute;
    display: flex;
    align-items: center;
    gap: 12px;
    font-weight: 700;
    letter-spacing: -0.5px;
    white-space: nowrap;
  }
  .brand__mark {
    width: 20px;
    height: 20px;
    border-radius: 50%;
    background: var(--grass);
  }
  .card--front .brand { left: 28px; top: 42px; font-size: 36px; color: var(--ink); }
  .card--back .brand { left: 50%; top: 50%; transform: translate(-50%, -50%); font-size: 64px; color: var(--paper); }
  .card--back .brand__mark { width: 30px; height: 30px; background: var(--lime); }
  .contact {
    position: absolute;
    right: 26px;
    top: 68px;
    text-align: right;
    color: var(--paper);
  }
  .contact__name { font-size: 22px; font-weight: 700; margin: 0; }
  .contact__role { font-size: 12px; margin: 3px 0 12px; }
  .contact__line {
    display: flex;
    justify-content: flex-end;
    align-items: center;
    gap: 6px;
    font-size: 13px;
    margin: 4px 0;
    white-space: nowrap;
  }
  .contact__icon { width: 11px; height: 11px; fill: var(--paper); }
</style>
</head>
<body>
<main class="sheet">
  <section class="card card--front">
    <svg class="card__wave" viewBox="0 0 540 309" preserveAspectRatio="none" aria-hidden="true">
      <defs>
        <path id="wave-edge" d="M415,0 C345,20 325,120 265,190 C205,260 100,290 0,300 L-60,306 L-60,340 L620,340 L620,-40 L430,-40 Z"/>
      </defs>
      <use href="#wave-edge" transform="translate(-42,-14)" fill="var(--lime)"/>
      <use href="#wave-edge" transform="translate(-30,-10)" fill="var(--paper)"/>
      <use href="#wave-edge" transform="translate(-22,-7)" fill="var(--grass)"/>
      <use href="#wave-edge" transform="translate(-9,-3)" fill="var(--paper)"/>
      <use href="#wave-edge" fill="var(--leaf)"/>
    </svg>
    <div class="brand"><span class="brand__mark"></span>GreenReach</div>
    <div class="contact">
      <p class="contact__name">Daniel Harlow</p>
      <p class="contact__role">Project Manager</p>
      <p class="contact__line">555-014-0250 ext. 209
        <svg class="contact__icon" viewBox="0 0 12 12"><path d="M2.5 0.5l2 2.5-1 1.2c.7 1.5 1.8 2.6 3.3 3.3l1.2-1 2.5 2-1 2.5C5 10.5 1.5 7 0 1.5z"/></svg>
      </p>
      <p class="contact__line">555-016-1271
        <svg class="contact__icon" viewBox="0 0 12 12"><rect x="3" y="0" width="6" height="3"/><rect x="0" y="4" width="12" height="5" rx="1"/><rect x="3" y="8" width="6" height="4"/></svg>
      </p>
      <p class="contact__line">dan@greenreachlandscape.com
        <svg class="contact__icon" viewBox="0 0 12 12"><path d="M0 2h12v8H0z M1 3l5 4 5-4" stroke="var(--leaf)" stroke-width="0.8"/></svg>
      </p>
    </div>
  </section>

  <section class="card card--back">
    <div class="brand"><span class="brand__mark"></span>GreenReach</div>
  </section>
</main>
</body>
</html>
```